I would like a minimalist clean and uncluttered website design.
Initially, I would like to see a front page only and would then like to build on the project front there.
RTV logo file with no background is attached, can be grey scale if the designer wishes.
I would like the front page to speak about the company's ethos and goals and I will need to put a great deal of thought into this to ensure it has the desired impact with the content on the subsequent pages.
The paragraph below gives a bit of an idea as to what this will include.
"RTV is a technology company providing approachable IT products and services to business:
With the overwhelming advancements in technology, businesses often find it difficult to determine what is available and what best suits their businesses specific needs.
We can assist business with their IT infrustucture, devices, software in procurement, installation, training, cost control as well as ongoing administration and support. We also keep our Clients informed of new technology and products which can benefit them"
Target Market(s)
Business, Health, Education, Professional Practices. Target age would be around 30 plus either male or female. Office administration level through Managing Directors. English speaking.

```html
<!DOCTYPE html>
<html lang="en">
<head>
<meta charset="utf-8">
<title>RTV – RightTechView</title>
<link rel="stylesheet" href="https://fonts.googleapis.com/css2?family=Questrial&family=Open+Sans:ital,wght@0,300;0,400;1,300&display=swap">
<style>
:root{
  --green:#8dbb4c;
  --navy:#35477f;
  --navy-dark:#26325c;
  --text:#4a4a4a;
  --muted:#6d6d6d;
  --line:#e6e6e6;
  --footer:#f2f2f2;
  --social:#5a5a5a;
  --white:#ffffff;
}
*{margin:0;padding:0;box-sizing:border-box}
html,body{width:1200px;height:981px;overflow:hidden;background:var(--white)}
body{position:relative;font-family:"Open Sans",sans-serif;color:var(--text)}
a{text-decoration:none;color:inherit}

.site-header{position:absolute;left:0;top:0;width:1200px;height:71px;background:var(--white)}
.brand{position:absolute;left:177px;top:12px;display:flex;align-items:center;gap:8px}
.brand-mark{width:14px;height:14px;background:var(--green)}
.brand-name{font-family:"Questrial",sans-serif;font-size:26px;color:var(--navy);letter-spacing:2px}
.main-nav{position:absolute;left:477px;top:0;display:flex;height:71px}
.main-nav a{font-family:"Questrial",sans-serif;font-size:14px;color:#555;padding:0 19px;line-height:69px;border-bottom:3px solid transparent}
.main-nav a.is-active{color:var(--green);border-bottom-color:var(--green)}
.account-links{position:absolute;left:918px;top:28px;display:flex;font-size:10px;color:#999;font-family:"Questrial",sans-serif}
.account-links a{padding:0 10px}
.account-links a+a{border-left:1px solid #ddd}

.hero{position:absolute;left:0;top:71px;width:1200px;height:394px;background:linear-gradient(90deg,#3a3b3d 0%,#56585b 45%,#4b4c4e 70%,#2f3031 100%)}
.hero-people{position:absolute;left:555px;top:0;width:470px;height:394px;background:radial-gradient(ellipse at 55% 45%,#8a8c90 0%,#5f6165 55%,rgba(70,72,75,0) 80%)}
.hero-copy{position:absolute;left:173px;top:127px}
.hero-title{font-family:"Questrial",sans-serif;font-weight:400;font-size:30px;color:var(--white);margin-bottom:8px}
.hero-lead{font-weight:300;font-style:italic;font-size:16.5px;line-height:23px;color:#d8d8d8}
.btn-primary{display:inline-block;margin-top:20px;background:var(--green);color:var(--white);font-family:"Questrial",sans-serif;font-size:13px;width:115px;height:31px;line-height:31px;text-align:center}
.slider-dots{position:absolute;left:174px;top:342px;display:flex;gap:3px}
.slider-dots span{width:13px;height:13px;border-radius:50%;background:var(--white)}
.slider-dots span.is-current{box-shadow:inset 0 0 0 3px var(--white);background:var(--navy)}

.services-ribbon{position:absolute;left:437px;top:508px}
.services-ribbon span{position:absolute;left:30px;top:0;width:228px;height:39px;line-height:39px;text-align:center;font-family:"Questrial",sans-serif;font-size:25px;color:var(--white)}

.service{position:absolute;width:230px}
.service-title{display:flex;align-items:center;gap:9px;font-family:"Questrial",sans-serif;font-weight:400;font-size:17px;color:var(--navy);height:24px}
.service-title svg{fill:var(--navy)}
.service p{margin-top:8px;font-size:11px;line-height:14.5px;color:var(--muted)}

.site-footer{position:absolute;left:0;top:890px;width:1200px;height:91px;background:var(--footer);border-top:1px solid var(--line)}
.footer-nav{position:absolute;left:171px;top:37px;font-size:10.5px;color:#555}
.footer-nav .sep{margin:0 6px;color:#888}
.social{position:absolute;left:946px;top:36px;display:flex;gap:4px}
.social span{width:17px;height:17px;border-radius:50%;background:var(--social)}
</style>
</head>
<body>
<header class="site-header">
  <a class="brand" href="#"><span class="brand-mark"></span><span class="brand-name">RTV</span></a>
  <nav class="main-nav">
    <a class="is-active" href="#">Home</a>
    <a href="#">Services</a>
    <a href="#">Project</a>
    <a href="#">Articles</a>
    <a href="#">Contact</a>
  </nav>
  <div class="account-links"><a href="#">Log in</a><a href="#">Sign up</a></div>
</header>

<section class="hero" role="img" aria-label="Blurred office background">
  <div class="hero-people" role="img" aria-label="Photo of three smiling business professionals, a woman holding a laptop in front"></div>
  <div class="hero-copy">
    <h1 class="hero-title">Welcome to RightTechView</h1>
    <p class="hero-lead">RTV is a technology company providing<br>approachable IT products and services to business.</p>
    <a class="btn-primary" href="#">LEARN MORE</a>
  </div>
  <div class="slider-dots"><span></span><span class="is-current"></span><span></span><span></span></div>
</section>

<div class="services-ribbon">
  <svg width="290" height="50" viewBox="0 0 290 50">
    <polygon points="0,10 40,10 40,49 0,49 12,30" fill="var(--navy)"/>
    <polygon points="290,10 250,10 250,49 290,49 278,30" fill="var(--navy)"/>
    <polygon points="30,39 40,39 40,49" fill="var(--navy-dark)"/>
    <polygon points="260,39 250,39 250,49" fill="var(--navy-dark)"/>
    <rect x="30" y="0" width="230" height="39" fill="var(--navy)"/>
  </svg>
  <span>OUR SERVICES</span>
</div>

<article class="service" style="left:173px;top:618px">
  <h2 class="service-title"><svg width="24" height="22" viewBox="0 0 24 22"><path d="M1 1h22v15H1z" fill="none" stroke="var(--navy)" stroke-width="2"/><rect x="10" y="16" width="4" height="3"/><rect x="7" y="19" width="10" height="2"/></svg>IT infrustucture</h2>
  <p>Lorem Ipsum is simply dummy text of the printing and typesetting industry. Lorem Ipsum dummy text ever since the 1500s...</p>
</article>
<article class="service" style="left:483px;top:618px">
  <h2 class="service-title"><svg width="16" height="22" viewBox="0 0 16 22"><rect x="1" y="1" width="14" height="20" rx="2" fill="none" stroke="var(--navy)" stroke-width="2"/><rect x="6" y="17" width="4" height="1.5"/></svg>Devices</h2>
  <p>Lorem Ipsum is simply dummy text of the printing and typesetting industry. Lorem Ipsum dummy text ever since the 1500s...</p>
</article>
<article class="service" style="left:792px;top:618px">
  <h2 class="service-title"><svg width="24" height="22" viewBox="0 0 24 22"><polygon points="12,1 23,6 12,11 1,6"/><polygon points="1,8 11,13 11,21 1,16" opacity=".85"/><polygon points="13,13 23,8 23,16 13,21" opacity=".7"/></svg>Software</h2>
  <p>Lorem Ipsum is simply dummy text of the printing and typesetting industry. Lorem Ipsum dummy text ever since the 1500s...</p>
</article>
<article class="service" style="left:173px;top:746px">
  <h2 class="service-title"><svg width="18" height="24" viewBox="0 0 18 24"><rect x="1" y="1" width="16" height="2"/><rect x="1" y="21" width="16" height="2"/><path d="M3 3 Q3 10 9 12 Q3 14 3 21 M15 3 Q15 10 9 12 Q15 14 15 21" fill="none" stroke="var(--navy)" stroke-width="1.8"/><polygon points="5,20 13,20 9,15"/></svg>Installation</h2>
  <p>Lorem Ipsum is simply dummy text of the printing and typesetting industry. Lorem Ipsum dummy text ever since the 1500s...</p>
</article>
<article class="service" style="left:483px;top:746px">
  <h2 class="service-title"><svg width="22" height="22" viewBox="0 0 22 22"><rect x="5" y="3" width="3" height="10" rx="1.5"/><rect x="9" y="1" width="3" height="11" rx="1.5"/><rect x="13" y="3" width="3" height="10" rx="1.5"/><path d="M5 10h13v5l-4 6H8L3 14l2-2z"/><rect x="17" y="7" width="3" height="8" rx="1.5" transform="rotate(20 18 11)"/></svg>Training</h2>
  <p>Lorem Ipsum is simply dummy text of the printing and typesetting industry. Lorem Ipsum dummy text ever since the 1500s...</p>
</article>
<article class="service" style="left:792px;top:746px">
  <h2 class="service-title"><svg width="34" height="22" viewBox="0 0 34 22"><rect x="6" y="1" width="27" height="15" fill="none" stroke="var(--navy)" stroke-width="1.5"/><rect x="3" y="3.5" width="27" height="15" fill="var(--white)" stroke="var(--navy)" stroke-width="1.5"/><rect x="1" y="6" width="27" height="15" fill="var(--navy)"/><rect x="3.5" y="8.5" width="22" height="10" fill="none" stroke="var(--white)" stroke-width="1"/><circle cx="14.5" cy="13.5" r="3.5" fill="var(--white)"/></svg>Cost control</h2>
  <p>Lorem Ipsum is simply dummy text of the printing and typesetting industry. Lorem Ipsum dummy text ever since the 1500s...</p>
</article>

<footer class="site-footer">
  <nav class="footer-nav"><a href="#">Home</a><span class="sep">|</span><a href="#">Services</a><span class="sep">|</span><a href="#">Project</a><span class="sep">|</span><a href="#">Articles</a><span class="sep">|</span><a href="#">Contact</a><span class="sep">|</span>Copyright © 2013 RightTechView.</nav>
  <div class="social" aria-label="Social links"><span></span><span></span><span></span><span></span></div>
</footer>
</body>
</html>
```